Social Event Calendar for real estate ad

I need a one page - 8 1/2 x 11 card (front and back) designed to include a list of events and images. The design should look somewhat tropical and friendly utilizing the color Aqua Blue. I am a real estate broker in West Palm Beach, Florida.

Target Market(s)

Adult homeowners age 30-80 of Florida homes primarily in the West Palm Beach, Florida historic homes market. The purpose of the marketing piece is to provide interesting content on the social events occurring within the next 6 months in the area. The ad should portray the sender as an expert in the neighborhood. The call to action will be for the reader to contact the sender of the ad to determine the value of the reader's home.

Industry/Entity Type

Real Estate

Font styles to use
Other font styles liked:
• Helvetica

Colors
0092cd
00a990
e567a6

Requirements
Must have
• Must have a calendar listing of events similar to the screenshot provided but fitting 10 events for January and 10 for February.

```html
<!DOCTYPE html>
<html lang="en">
<head>
<meta charset="utf-8">
<title>Social Events Listing – West Palm Beach Real Estate</title>
<link href="https://fonts.googleapis.com/css2?family=Arimo:ital,wght@0,400;0,700;1,400&family=Oswald:wght@600&display=swap" rel="stylesheet">
<style>
  :root {
    --magenta: #df52e6;
    --magenta-box: #e24fe0;
    --green: #3ddc7a;
    --green-title: #4bd47e;
    --ink: #1c2b2a;
    --white: #ffffff;
    --sheet-top: #1f8fe0;
    --sheet-mid: #2bb8ea;
    --sheet-deep: #1565cf;
    --avatar: #8a9297;
  }
  html, body {
    margin: 0;
    padding: 0;
    width: 848px;
    height: 1200px;
    overflow: hidden;
    background: #ffffff;
  }
  .flyer {
    position: relative;
    width: 848px;
    height: 1200px;
    overflow: hidden;
    font-family: "Arimo", Helvetica, Arial, sans-serif;
  }
  .water-backdrop {
    position: absolute;
    inset: 114px 0 33px 0;
    background:
      radial-gradient(ellipse at 70% 20%, rgba(90, 230, 245, 0.85), transparent 60%),
      radial-gradient(ellipse at 10% 80%, rgba(30, 120, 220, 0.8), transparent 55%),
      linear-gradient(160deg, var(--sheet-top) 0%, var(--sheet-mid) 45%, var(--sheet-deep) 100%);
  }
  .masthead {
    position: absolute;
    top: 0;
    left: 0;
    width: 848px;
    height: 114px;
    background: var(--magenta);
  }
  .agent-photo {
    position: absolute;
    top: 0;
    left: 0;
    width: 94px;
    height: 114px;
    background: linear-gradient(180deg, #a4acb1, var(--avatar));
    box-shadow: inset 0 0 0 2px #5f6669;
  }
  .tagline {
    position: absolute;
    margin: 0;
    color: var(--white);
    font-weight: 700;
    font-size: 34px;
    line-height: 1;
    white-space: nowrap;
  }
  .tagline--first { top: 11px; left: 128px; }
  .tagline--second { top: 61px; right: 29px; }
  .listing-title {
    position: absolute;
    top: 122px;
    left: 0;
    width: 848px;
    margin: 0;
    text-align: center;
    font-size: 50px;
    font-weight: 400;
    line-height: 1.2;
    color: var(--green-title);
    -webkit-text-stroke: 1.5px #1e3b2a;
    letter-spacing: 0.5px;
  }
  .events {
    position: absolute;
    top: 0;
    left: 0;
  }
  .date-num {
    font-family: "Oswald", "Arial Narrow", sans-serif;
    font-weight: 600;
    font-size: 44px;
    fill: var(--white);
  }
  .date-month {
    font-family: "Oswald", "Arial Narrow", sans-serif;
    font-weight: 600;
    font-size: 25px;
    fill: var(--white);
  }
  .event-text {
    font-family: "Arimo", Helvetica, Arial, sans-serif;
    font-style: italic;
    font-size: 20.5px;
    fill: #2b3033;
  }
  .contact-bar {
    position: absolute;
    bottom: 0;
    left: 0;
    width: 848px;
    height: 33px;
    background: var(--green);
    color: var(--ink);
    font-weight: 700;
    font-size: 15px;
    display: flex;
    align-items: center;
    justify-content: center;
    gap: 10px;
    white-space: nowrap;
  }
</style>
</head>
<body>
<main class="flyer">
  <div class="water-backdrop" role="img" aria-label="Aqua blue splashing water background"></div>

  <header class="masthead">
    <div class="agent-photo" role="img" aria-label="Agent portrait"></div>
    <p class="tagline tagline--first">“Your #1 Real Estate Agent”</p>
    <p class="tagline tagline--second">“For West Palm Beach, Florida”</p>
  </header>

  <h1 class="listing-title">Social Events Listing</h1>

  <svg class="events" width="848" height="1200" viewBox="0 0 848 1200" xmlns="http://www.w3.org/2000/svg">
    <defs>
      <linearGradient id="arrowFillRight" x1="0" y1="0" x2="1" y2="1">
        <stop offset="0" stop-color="#c5cacd"/>
        <stop offset="0.35" stop-color="#eef1f2"/>
        <stop offset="1" stop-color="#d3d8db"/>
      </linearGradient>
      <linearGradient id="arrowFillLeft" x1="1" y1="0" x2="0" y2="1">
        <stop offset="0" stop-color="#c5cacd"/>
        <stop offset="0.35" stop-color="#eef1f2"/>
        <stop offset="1" stop-color="#d3d8db"/>
      </linearGradient>
      <radialGradient id="photoTone" cx="0.5" cy="0.4" r="0.65">
        <stop offset="0" stop-color="#a9c6e2"/>
        <stop offset="1" stop-color="#5f89b4"/>
      </radialGradient>
    </defs>

    <g role="img" aria-label="Scenic lakeside landscape photo">
      <circle cx="129" cy="402" r="83" fill="url(#photoTone)"/>
      <circle cx="129" cy="569" r="83" fill="url(#photoTone)"/>
      <circle cx="129" cy="735" r="83" fill="url(#photoTone)"/>
      <circle cx="129" cy="902" r="83" fill="url(#photoTone)"/>
      <circle cx="129" cy="1069" r="83" fill="url(#photoTone)"/>
    </g>
    <g role="img" aria-label="Scenic lakeside landscape photo">
      <circle cx="693" cy="287" r="83" fill="url(#photoTone)"/>
      <circle cx="693" cy="456" r="83" fill="url(#photoTone)"/>
      <circle cx="693" cy="622" r="83" fill="url(#photoTone)"/>
      <circle cx="693" cy="788" r="83" fill="url(#photoTone)"/>
      <circle cx="693" cy="956" r="83" fill="url(#photoTone)"/>
    </g>

    <g transform="translate(0,280)">
      <polygon points="339,0 565,0 565,-8 609,40 565,88 565,80 339,80" fill="url(#arrowFillRight)"/>
      <rect x="262" y="0" width="77" height="80" fill="var(--magenta-box)"/>
      <text class="date-num" x="300" y="46" text-anchor="middle">01</text>
      <text class="date-month" x="300" y="72" text-anchor="middle">JAN</text>
      <text class="event-text" x="357" y="30">open house event</text>
      <text class="event-text" x="357" y="55">palm beach</text>
    </g>
    <g transform="translate(0,360)">
      <polygon points="483,0 260,0 260,-8 216,40 260,88 260,80 483,80" fill="url(#arrowFillLeft)"/>
      <rect x="483" y="0" width="74" height="80" fill="var(--green)"/>
      <text class="date-num" x="520" y="46" text-anchor="middle">03</text>
      <text class="date-month" x="520" y="72" text-anchor="middle">JAN</text>
      <text class="event-text" x="301" y="30">your event listing</text>
      <text class="event-text" x="301" y="55">venue, address</text>
    </g>
    <g transform="translate(0,440)">
      <polygon points="339,0 565,0 565,-8 609,40 565,88 565,80 339,80" fill="url(#arrowFillRight)"/>
      <rect x="262" y="0" width="77" height="80" fill="var(--magenta-box)"/>
      <text class="date-num" x="300" y="46" text-anchor="middle">08</text>
      <text class="date-month" x="300" y="72" text-anchor="middle">JAN</text>
      <text class="event-text" x="357" y="30">open house event</text>
      <text class="event-text" x="357" y="55">palm beach</text>
    </g>
    <g transform="translate(0,519)">
      <polygon points="483,0 260,0 260,-8 216,40 260,88 260,80 483,80" fill="url(#arrowFillLeft)"/>
      <rect x="483" y="0" width="74" height="80" fill="var(--green)"/>
      <text class="date-num" x="520" y="46" text-anchor="middle">10</text>
      <text class="date-month" x="520" y="72" text-anchor="middle">JAN</text>
      <text class="event-text" x="301" y="30">your event listing</text>
      <text class="event-text" x="301" y="55">venue, address</text>
    </g>
    <g transform="translate(0,599)">
      <polygon points="339,0 565,0 565,-8 609,40 565,88 565,80 339,80" fill="url(#arrowFillRight)"/>
      <rect x="262" y="0" width="77" height="80" fill="var(--magenta-box)"/>
      <text class="date-num" x="300" y="46" text-anchor="middle">12</text>
      <text class="date-month" x="300" y="72" text-anchor="middle">JAN</text>
      <text class="event-text" x="357" y="30">open house event</text>
      <text class="event-text" x="357" y="55">palm beach</text>
    </g>
    <g transform="translate(0,678)">
      <polygon points="483,0 260,0 260,-8 216,40 260,88 260,80 483,80" fill="url(#arrowFillLeft)"/>
      <rect x="483" y="0" width="74" height="80" fill="var(--green)"/>
      <text class="date-num" x="520" y="46" text-anchor="middle">15</text>
      <text class="date-month" x="520" y="72" text-anchor="middle">JAN</text>
      <text class="event-text" x="301" y="30">your event listing</text>
      <text class="event-text" x="301" y="55">venue, address</text>
    </g>
    <g transform="translate(0,758)">
      <polygon points="339,0 565,0 565,-8 609,40 565,88 565,80 339,80" fill="url(#arrowFillRight)"/>
      <rect x="262" y="0" width="77" height="80" fill="var(--magenta-box)"/>
      <text class="date-num" x="300" y="46" text-anchor="middle">18</text>
      <text class="date-month" x="300" y="72" text-anchor="middle">JAN</text>
      <text class="event-text" x="357" y="30">open house event</text>
      <text class="event-text" x="357" y="55">palm beach</text>
    </g>
    <g transform="translate(0,837)">
      <polygon points="483,0 260,0 260,-8 216,40 260,88 260,80 483,80" fill="url(#arrowFillLeft)"/>
      <rect x="483" y="0" width="74" height="80" fill="var(--green)"/>
      <text class="date-num" x="520" y="46" text-anchor="middle">21</text>
      <text class="date-month" x="520" y="72" text-anchor="middle">JAN</text>
      <text class="event-text" x="301" y="30">your event listing</text>
      <text class="event-text" x="301" y="55">venue, address</text>
    </g>
    <g transform="translate(0,917)">
      <polygon points="339,0 565,0 565,-8 609,40 565,88 565,80 339,80" fill="url(#arrowFillRight)"/>
      <rect x="262" y="0" width="77" height="80" fill="var(--magenta-box)"/>
      <text class="date-num" x="300" y="46" text-anchor="middle">24</text>
      <text class="date-month" x="300" y="72" text-anchor="middle">JAN</text>
      <text class="event-text" x="357" y="30">open house event</text>
      <text class="event-text" x="357" y="55">palm beach</text>
    </g>
    <g transform="translate(0,996)">
      <polygon points="483,0 296,0 296,76 483,76" fill="url(#arrowFillLeft)"/>
      <rect x="483" y="0" width="74" height="76" fill="var(--green)"/>
      <text class="date-num" x="520" y="44" text-anchor="middle">25</text>
      <text class="date-month" x="520" y="70" text-anchor="middle">JAN</text>
      <text class="event-text" x="301" y="30">your event listing</text>
      <text class="event-text" x="301" y="55">venue, address</text>
    </g>
  </svg>

  <footer class="contact-bar">
    <span>Direct Line: 000.000.0000</span><span>|</span>
    <span>Email: name@realestate.com</span><span>|</span>
    <span>Website: www.yourwebsite.com</span>
  </footer>
</main>
</body>
</html>
```